Golden Pantry Spice

Distributor of seasonings and spices to the restaurant industry.

Industry/Entity Type

Restaurant

Contact Information for Business Card

Golden Pantry
Derek Hollings
TW Brandvik Distributor
316-487-9021
derek@goldpantryspicehub.com

No minimum order
Gluten & MSG free soup bases

```html
<!DOCTYPE html>
<html lang="en">
<head>
<meta charset="utf-8">
<title>Golden Pantry Spice – Business Card</title>
<link rel="stylesheet" href="https://fonts.googleapis.com/css2?family=Open+Sans:wght@400;600;700&display=swap">
<style>
  :root {
    --bg: #c9c9c9;
    --orange: #e07020;
    --white: #ffffff;
    --charcoal: #2b2b2b;
    --charcoal-light: #363636;
    --ink: #1a1a1a;
    --text-light: #f2f2f2;
    --text-muted: #d6d6d6;
  }
  * { box-sizing: border-box; margin: 0; padding: 0; }
  html, body {
    width: 1200px; height: 970px; overflow: hidden;
    background: var(--bg);
    font-family: "Open Sans", Arial, sans-serif;
  }
  .business-card {
    position: absolute; left: 400px; top: 135px;
    width: 400px; height: 700px;
    background: var(--charcoal);
    display: flex; flex-direction: column;
  }
  .edge-band { height: 28px; background: var(--orange); flex: none; }
  .brand-zone {
    height: 232px; background: var(--white);
    display: flex; align-items: center; justify-content: center; gap: 14px;
  }
  .brand-dot { width: 22px; height: 22px; border-radius: 50%; background: var(--orange); flex: none; }
  .brand-name {
    font-weight: 700; font-size: 30px; line-height: 1.15; color: var(--ink);
  }
  .identity { text-align: center; padding-top: 52px; }
  .person-name { color: var(--text-light); font-weight: 600; font-size: 25px; letter-spacing: 1px; }
  .person-role { color: var(--text-muted); font-size: 14px; letter-spacing: 0.5px; margin-top: 2px; }
  .contact-strip {
    margin-top: 40px; background: var(--charcoal-light);
    padding: 20px 0 22px 38px; display: flex; flex-direction: column; gap: 14px;
  }
  .contact-line { display: flex; align-items: center; gap: 16px; color: var(--text-light); font-size: 17px; }
  .contact-line svg { width: 30px; height: 24px; flex: none; }
  .selling-points {
    list-style: none; text-align: center; color: var(--orange);
    font-weight: 600; font-size: 20px; line-height: 1.3;
    margin-top: 52px;
  }
  .selling-points li::before { content: "• "; }
  .spacer { flex: 1; }
</style>
</head>
<body>
  <article class="business-card">
    <div class="edge-band"></div>
    <header class="brand-zone">
      <span class="brand-dot"></span>
      <span class="brand-name">Golden Pantry<br>Spice</span>
    </header>
    <section class="identity">
      <h1 class="person-name">DEREK HOLLINGS</h1>
      <p class="person-role">TW Brandvik Distributor</p>
    </section>
    <section class="contact-strip">
      <div class="contact-line">
        <svg viewBox="0 0 30 24" aria-hidden="true">
          <path d="M2 8 Q15 0 28 8 L26 11 L21 10 L20 7 Q15 5 10 7 L9 10 L4 11 Z" fill="#fff"/>
          <path d="M7 12 L23 12 L26 22 L4 22 Z" fill="#fff"/>
          <circle cx="15" cy="17" r="3" fill="#363636"/>
        </svg>
        <span>316-487-9021</span>
      </div>
      <div class="contact-line">
        <svg viewBox="0 0 30 24" aria-hidden="true">
          <rect x="1" y="3" width="28" height="18" fill="#fff"/>
          <path d="M1 3 L15 14 L29 3" fill="none" stroke="#363636" stroke-width="1.6"/>
          <path d="M1 21 L11 11 M29 21 L19 11" stroke="#363636" stroke-width="1.2"/>
        </svg>
        <span>derek@goldpantryspicehub.com</span>
      </div>
    </section>
    <ul class="selling-points">
      <li>No minimum order</li>
      <li>Gluten &amp; MSG free soup bases</li>
    </ul>
    <div class="spacer"></div>
    <div class="edge-band"></div>
  </article>
</body>
</html>
```